Product Designer Business Card

Small product design, engineering and prototyping firm in need of a clean, professional business card design. To support our 3D design and drawing services, we offer 3D printing, molding, and casting of plastics, silicones, resins, etc. Our logo can still be modified/changed if necessary. The red/orange color is preferred, but may be substituted with blue or green, potentially. Either way, the colour of the logo should be match/compliment colors used throughout the design. One thought is to have the logo/contact info on one side, with the other side describing services offered, like with a small icon of 3D printer, molding, casting, and computer with a 3D model on-screen.
Industry/Entity Type
Mechanical Engineering
Contact Information for Business Card
Company: Velkin Design
Phone: 613-555-0147
Email: marc@velkindesign.ca

```html
<!DOCTYPE html>
<html lang="en">
<head>
<meta charset="utf-8">
<title>Velkin Design — Business Card</title>
<link rel="stylesheet" href="https://fonts.googleapis.com/css2?family=Montserrat:wght@400;500;600&display=swap">
<style>
  :root {
    --backdrop: #d0d1cc;
    --card-white: #ffffff;
    --brand-red: #de1f00;
    --brand-deep: #7a0d08;
    --text-grey: #555555;
    --icon-tint: rgba(255, 255, 255, 0.18);
    --icon-line: rgba(255, 255, 255, 0.85);
  }
  * { box-sizing: border-box; margin: 0; padding: 0; }
  html, body {
    width: 1200px;
    height: 1058px;
    overflow: hidden;
    background: var(--backdrop);
    font-family: "Montserrat", Arial, sans-serif;
  }
  .canvas {
    position: relative;
    width: 1200px;
    height: 1058px;
  }
  .card {
    position: absolute;
    left: 320px;
    width: 560px;
    height: 320px;
    overflow: hidden;
    box-shadow: 0 12px 30px rgba(0, 0, 0, 0.18);
  }
  .card--front { top: 160px; background: var(--card-white); }
  .card--back  { top: 560px; background: var(--brand-red); }

  .wordmark {
    position: absolute;
    display: flex;
    align-items: center;
    gap: 12px;
    font-weight: 600;
    letter-spacing: 0.05em;
    white-space: nowrap;
  }
  .wordmark__dot {
    border-radius: 50%;
    flex: none;
  }
  .card--front .wordmark {
    left: 36px; top: 143px;
    font-size: 23px;
    color: var(--brand-deep);
  }
  .card--front .wordmark__dot {
    width: 26px; height: 26px;
    background: var(--brand-deep);
  }
  .card--back .wordmark {
    left: 44px; top: 132px;
    font-size: 36px;
    color: var(--card-white);
  }
  .card--back .wordmark__dot {
    width: 40px; height: 40px;
    background: var(--card-white);
  }

  .divider {
    position: absolute;
    left: 318px; top: 90px;
    width: 1px; height: 140px;
    background: linear-gradient(to bottom, transparent, var(--brand-red), transparent);
  }
  .contact {
    position: absolute;
    left: 340px; top: 104px;
  }
  .contact__name {
    font-size: 20px;
    font-weight: 500;
    color: var(--brand-red);
    letter-spacing: 0.01em;
    white-space: nowrap;
  }
  .contact__role {
    font-size: 14px;
    color: var(--text-grey);
    margin: 2px 0 12px;
    letter-spacing: 0.04em;
  }
  .contact__line {
    display: flex;
    align-items: center;
    gap: 8px;
    font-size: 14px;
    color: var(--text-grey);
    line-height: 22px;
    letter-spacing: 0.02em;
    white-space: nowrap;
  }
  .contact__icon { width: 11px; height: 11px; flex: none; }

  .services {
    position: absolute;
    right: 30px; top: 22px;
    display: flex;
    flex-direction: column;
    gap: 14px;
    align-items: center;
  }
  .service {
    display: flex;
    flex-direction: column;
    align-items: center;
    gap: 4px;
  }
  .service__icon {
    width: 62px; height: 58px;
    background: var(--icon-tint);
    border: 2px solid var(--icon-line);
    border-radius: 4px;
  }
  .service__label {
    font-size: 12px;
    font-weight: 500;
    color: var(--card-white);
    letter-spacing: 0.03em;
  }
</style>
</head>
<body>
<main class="canvas">

  <section class="card card--front" aria-label="Business card front">
    <div class="wordmark">
      <span class="wordmark__dot"></span>
      <span class="wordmark__name">Velkin Design</span>
    </div>
    <div class="divider"></div>
    <div class="contact">
      <p class="contact__name">ALDRIC THORNE</p>
      <p class="contact__role">President</p>
      <p class="contact__line">
        <svg class="contact__icon" viewBox="0 0 12 12" aria-hidden="true">
          <path d="M3 1 L5 3.5 L4 5 Q5 7 7 8 L8.5 7 L11 9 L10 11 Q5 11 1 5 Q1 2 3 1 Z" fill="#de1f00"/>
        </svg>
        613-555-0147
      </p>
      <p class="contact__line">
        <svg class="contact__icon" viewBox="0 0 12 12" aria-hidden="true">
          <rect x="1" y="2.5" width="10" height="7" fill="none" stroke="#de1f00" stroke-width="1.3"/>
          <path d="M1 2.5 L6 6.5 L11 2.5" fill="none" stroke="#de1f00" stroke-width="1.3"/>
        </svg>
        marc@velkindesign.ca
      </p>
    </div>
  </section>

  <section class="card card--back" aria-label="Business card back">
    <div class="wordmark">
      <span class="wordmark__dot"></span>
      <span class="wordmark__name">Velkin Design</span>
    </div>
    <div class="services">
      <div class="service">
        <div class="service__icon" role="img" aria-label="Line icon of a molding machine"></div>
        <span class="service__label">Molding</span>
      </div>
      <div class="service">
        <div class="service__icon" role="img" aria-label="Line icon of a 3D printer"></div>
        <span class="service__label">3D printer</span>
      </div>
      <div class="service">
        <div class="service__icon" role="img" aria-label="Line icon for casting"></div>
        <span class="service__label">Casting</span>
      </div>
    </div>
  </section>

</main>
</body>
</html>
```